Business Consulting Company needs a business card designed

We need a business card in Brisbane Australia for a company called " Marrowvale Consulting Group". I would like to see the designs either in purple or green color

```html
<!DOCTYPE html>
<html lang="en">
<head>
<meta charset="utf-8">
<title>Marrowvale Consulting Group – Business Card</title>
<link rel="stylesheet" href="https://fonts.googleapis.com/css2?family=Open+Sans:wght@400;600;700&display=swap">
<style>
  :root {
    --page-bg: #e6e6e9;
    --card-bg: #ffffff;
    --brand-purple: #7b2f9e;
    --text-grey: #3c3c3c;
    --muted-grey: #5a5a5a;
    --rule-grey: #4a4a4a;
  }
  * { margin: 0; padding: 0; box-sizing: border-box; }
  html, body {
    width: 1200px;
    height: 720px;
    overflow: hidden;
    background: var(--page-bg);
    font-family: "Open Sans", Arial, sans-serif;
  }
  .card {
    position: absolute;
    left: 100px;
    top: 74px;
    width: 1000px;
    height: 572px;
    background: var(--card-bg);
    box-shadow: 0 10px 30px rgba(0, 0, 0, 0.18);
  }
  .brand {
    position: absolute;
    left: 0;
    top: 0;
    width: 460px;
    height: 100%;
    display: flex;
    flex-direction: column;
    align-items: center;
    justify-content: center;
    gap: 22px;
  }
  .brand-mark {
    width: 70px;
    height: 70px;
    border-radius: 50%;
    background: var(--brand-purple);
  }
  .brand-name {
    color: var(--brand-purple);
    font-weight: 600;
    font-size: 44px;
    line-height: 1.1;
    letter-spacing: 2px;
    text-transform: uppercase;
    text-align: center;
  }
  .divider {
    position: absolute;
    left: 460px;
    top: 24px;
    width: 3px;
    height: 500px;
    background: var(--rule-grey);
  }
  .details {
    position: absolute;
    left: 500px;
    top: 36px;
    right: 40px;
    color: var(--text-grey);
  }
  .person-name {
    color: var(--brand-purple);
    font-weight: 700;
    font-size: 30px;
    line-height: 1.1;
  }
  .person-role {
    font-size: 19px;
    letter-spacing: 1px;
    text-transform: uppercase;
    color: var(--muted-grey);
  }
  .address {
    margin-top: 44px;
    font-size: 21px;
    line-height: 1.3;
  }
  .contact {
    margin-top: 72px;
    font-size: 21px;
    line-height: 1.35;
    list-style: none;
  }
  .contact-label { font-weight: 700; margin-right: 6px; }
  .contact .email { margin-top: 14px; }
</style>
</head>
<body>
  <main class="card">
    <section class="brand">
      <span class="brand-mark" aria-hidden="true"></span>
      <h1 class="brand-name">Marrowvale<br>Consulting<br>Group</h1>
    </section>

    <div class="divider" aria-hidden="true"></div>

    <section class="details">
      <h2 class="person-name">Daniel Harcourt</h2>
      <p class="person-role">Founder</p>

      <address class="address">
        58 Kessler Rd,<br>
        Ashgrove Park Queensland 4060<br>
        Australia
      </address>

      <ul class="contact">
        <li><span class="contact-label">P</span>+1 (555) 014 - 2290</li>
        <li><span class="contact-label">F</span>+1 (555) 014 - 3381</li>
        <li class="email">daniel.harcourt@marrowvalegroup.com</li>
      </ul>
    </section>
  </main>
</body>
</html>
```